Company selling food supplements with CBD needs label.

We need a label design for a company called "VEX Lab ltd", is based in the UK, the market name is "VEX" or "VEX Velvet Ember Xtracts". The initial product is Virgin Organic Hemp Seed Oil with a CBD in a 10ml amber dropper bottle. The design should be simplicity and luxury. The design should include also box.

Target Market(s)

Food supplements on Pellmart UK

Industry/Entity Type

Supplement

Font styles to use
Other font styles liked:
• Some luxury

Colors

Designer to choose colors to be used in the design.

Requirements
Must have
• All the information on the label required by the UK for the food supplements, the same on the box. One version matt one transparent. The design should include different CBD content, one different bottle (250mg, 500mg, 750mg, 1000mg) .
• The label and box should include the following phrases: "DIRECTIONS: Food Supplement. Shake well before use. Use 4-6 drops 2-3 times a day. Leave the oil in your mouth for 30-60 seconds before swallowing. Gradually build up the dose to find your optimum dosage.
• CAUTION: Do not exceed the recommended daily intake. Do not use as a substitute for a varied diet. Do not use during pregnancy and breastfeeding. Store in a dark and cool place, away from sunlight. Keep away from children.
• INGREDIENTS: Hemp Seed Oil, Omega-6 (2800mg), Omega-3 (930mg), CBD (250mg)
• MANUFACTURED: VEX Lab Ltd, 87 Quillon Rd, Harrow, KT9 4PW, www,vexlabuk.co.uk, info@vexlabuk.co.uk.
• EXPIRED DATE: "
• The box should also include a place for bark code.
Nice to have
• Simple and elegant design vertical or horizontal with exposed company logo "VEX" or "VEX Velvet Ember Xtracts". The company logo is provided but designers may change it freely.
Should not have
• The best without pictures/graphics overloading simplicity and purity of design.

```html
<!DOCTYPE html>
<html lang="en">
<head>
<meta charset="utf-8">
<title>VEX Hemp Seed Oil with CBD – Label</title>
<link rel="stylesheet" href="https://fonts.googleapis.com/css2?family=Lato:wght@400;700;900&family=Roboto+Condensed:wght@400&display=swap">
<style>
  :root {
    --canvas: #eef0f1;
    --charcoal: #2b2c2d;
    --neon-green: #2ee62a;
    --label-green: #34e82b;
    --ink: #111111;
    --paper: #ffffff;
    --panel-tint: #d2f7cf;
  }
  * { margin: 0; padding: 0; box-sizing: border-box; }
  html, body {
    width: 812px; height: 1200px; overflow: hidden;
    background: var(--canvas);
  }
  .canvas { position: relative; width: 812px; height: 1200px; }
  .label {
    position: absolute; left: 6px; top: 400px;
    width: 800px; height: 400px;
    background: var(--paper);
    box-shadow: 0 10px 24px rgba(0,0,0,0.25);
    overflow: hidden;
  }
  .label-front { position: absolute; left: 0; top: 0; width: 400px; height: 400px; }
  .label-front svg.front-shapes { position: absolute; inset: 0; }
  .brand-name {
    position: absolute; left: 0; width: 400px; top: 30px;
    text-align: center;
    font-family: "Lato", sans-serif; font-weight: 700;
    font-size: 104px; line-height: 1; letter-spacing: 2px;
    color: var(--neon-green);
  }
  .brand-tagline {
    position: absolute; left: 0; width: 400px; top: 130px;
    text-align: center;
    font-family: "Roboto Condensed", sans-serif; font-weight: 400;
    font-size: 21px; color: var(--neon-green); letter-spacing: 0.5px;
  }
  .product-grade {
    position: absolute; left: 0; width: 400px; top: 198px;
    text-align: center;
    font-family: "Lato", sans-serif; font-weight: 700;
    font-size: 20px; color: var(--neon-green);
  }
  .product-name {
    position: absolute; left: 0; width: 400px; top: 244px;
    text-align: center;
    font-family: "Lato", sans-serif; font-weight: 900;
    font-size: 41px; line-height: 44px; color: var(--ink);
    letter-spacing: -0.5px;
  }
  .product-volume {
    position: absolute; left: 0; width: 400px; top: 368px;
    text-align: center;
    font-family: "Lato", sans-serif; font-weight: 700;
    font-size: 15px; color: var(--neon-green);
  }
  .label-back { position: absolute; left: 400px; top: 0; width: 400px; height: 400px; }
  .info-panel {
    position: absolute; left: 22px; top: 23px; width: 360px; height: 352px;
    border-radius: 20px;
    background: linear-gradient(90deg, var(--paper) 0%, var(--paper) 35%, var(--panel-tint) 100%);
  }
  .info-text {
    position: absolute; left: 37px; top: 40px; width: 330px;
    font-family: "Lato", sans-serif; font-size: 12.4px; line-height: 13.9px;
    color: var(--ink);
  }
  .info-block { margin-bottom: 13px; }
  .info-block:last-child { margin-bottom: 0; }
  .info-heading { font-weight: 700; color: var(--neon-green); }
</style>
</head>
<body>
<main class="canvas">
  <article class="label">
    <section class="label-front">
      <svg class="front-shapes" width="400" height="400" viewBox="0 0 400 400" aria-hidden="true">
        <rect x="0" y="0" width="400" height="400" fill="var(--label-green)"/>
        <path d="M0 0 H400 V188 H357 L312 230 H104 L57 188 H0 Z" fill="var(--charcoal)"/>
        <path d="M118 400 L145 366 H275 L302 400 Z" fill="var(--charcoal)"/>
      </svg>
      <div class="brand-name">VEX</div>
      <div class="brand-tagline">Velvet Ember Xtracts</div>
      <div class="product-grade">VIRGIN ORGANIC</div>
      <h1 class="product-name">HEMP SEED OIL<br>WITH CBD</h1>
      <div class="product-volume">10 ml</div>
    </section>

    <section class="label-back">
      <div class="info-panel"></div>
      <div class="info-text">
        <div class="info-block">
          <div class="info-heading">Ingredients:</div>
          Hemp Seed Oil, Omega-6 (2800mg), Omega-3 (930mg), CBD (250mg)
        </div>
        <div class="info-block">
          <div class="info-heading">Directions:</div>
          Food Supplement. Shake well before use. Use 4-6 drops 2-3 times a day. Leave the oil in your mouth for 30-60 seconds before swallowing. Gradually build up the dose to find your optimum dosage.
        </div>
        <div class="info-block">
          <div class="info-heading">Caution:</div>
          Do not exceed the recommended daily intake. Do not use as a substitute for a varied diet. Do not use during pregnancy and breastfeeding. Store in a dark and cool place, away from sunlight. Keep away from children.
        </div>
        <div class="info-block">
          <div class="info-heading">Manufactured and Distributed by</div>
          VEX Lab Ltd, 87 Quillon Rd, Harrow, KT9 4PW<br>
          www,vexlabuk.co.uk | info@vexlabuk.co.uk<br>
          Expiry date:
        </div>
      </div>
    </section>
  </article>
</main>
</body>
</html>
```